New letter head for Air Conditioning business

We need a new professional letter head design to suit our new re-branded air conditioning business. Our new logo is attached

```html
<!DOCTYPE html>
<html lang="en">
<head>
<meta charset="utf-8">
<title>Northwind Letterhead</title>
<link rel="stylesheet" href="https://fonts.googleapis.com/css2?family=Montserrat:wght@400;600&display=swap">
<style>
  :root {
    --ink: #3a3a3c;
    --text: #1f1f1f;
    --green: #66c38a;
    --paper: #ffffff;
  }
  html, body {
    margin: 0;
    padding: 0;
    overflow: hidden;
    background: var(--paper);
  }
  .letterhead {
    position: relative;
    width: 849px;
    height: 1200px;
    background: var(--paper);
    font-family: "Montserrat", Arial, sans-serif;
    color: var(--text);
    overflow: hidden;
  }
  .brand {
    position: absolute;
    left: 56px;
    top: 62px;
    display: flex;
    align-items: center;
    gap: 14px;
  }
  .brand-dot {
    width: 30px;
    height: 30px;
    border-radius: 50%;
    background: var(--green);
  }
  .brand-name {
    font-size: 42px;
    font-weight: 600;
    color: var(--ink);
    letter-spacing: 1px;
    line-height: 1;
  }
  .address {
    position: absolute;
    right: 51px;
    top: 62px;
    margin: 0;
    font-size: 13.4px;
    line-height: 20px;
    text-align: right;
    font-style: normal;
    letter-spacing: 0.2px;
  }
  .margin-rule {
    position: absolute;
    left: 797px;
    top: 121px;
    width: 2px;
    height: 676px;
    background: var(--green);
  }
  .contact {
    position: absolute;
    right: 51px;
    top: 823px;
    margin: 0;
    font-size: 13.4px;
    line-height: 20px;
    text-align: right;
    letter-spacing: 0.2px;
  }
  .contact p {
    margin: 0 0 12px;
  }
</style>
</head>
<body>
  <main class="letterhead">
    <header class="brand">
      <span class="brand-dot"></span>
      <span class="brand-name">Northwind</span>
    </header>

    <address class="address">
      Address here Address here Address here<br>
      Address here Address here Address here
    </address>

    <div class="margin-rule"></div>

    <footer class="contact">
      <p>Contact No<br>Email Adds</p>
      <p>Social Media<br>Website</p>
    </footer>
  </main>
</body>
</html>
```